Lawn mowing business card design

We need a business card design for our lawn mowing and gardening business which is located in the Northern Beaches of Sydney. Our business name is Meadowline Turf and our logo is predominantly green and yellow in color. Please see our website at www.meadowlineturf.com.au for design ideas. The business targets young professionals and older clientele. As such the font should be easy to read, but I also want the business card to be colorful and stand out.

Target Market(s)

young professionals

Industry/Entity Type

Lawn Care

Contact Information for Business Card

Meadowline Turf, Gareth Pellow, 0478559201, www.meadowlineturf.com.au, email: meadowlineturf@mailbox-example.com

Font styles to use
Serif

Colors
9bcb3b
fbed22

Requirements
Must have
• Must include the details listed above. Must include the attached logo.
Nice to have
• Logo attached with two copies. The logo without any writing is high quality, please feel free to be creative with the text stating our business name "Meadowline Turf" using this file.

```html
<!DOCTYPE html>
<html lang="en">
<head>
<meta charset="utf-8">
<title>Meadowline Turf – Business Card</title>
<link href="https://fonts.googleapis.com/css2?family=Didact+Gothic&display=swap" rel="stylesheet">
<style>
  :root {
    --page-bg: #d9dbd6;
    --card-bg: #ffffff;
    --ink: #1c1c1c;
    --brand-ink: #4a3a2a;
    --brand-green: #5cb82e;
    --grass-light: #b6e35a;
    --grass-mid: #7fcf35;
    --grass-deep: #56b325;
    --soil: #4b3a2e;
    --subsoil: #5e574e;
  }
  * { margin: 0; padding: 0; box-sizing: border-box; }
  html, body {
    width: 1200px; height: 1200px; overflow: hidden;
    background: var(--page-bg);
    font-family: "Didact Gothic", "Century Gothic", sans-serif;
    color: var(--ink);
  }
  .card {
    position: absolute;
    left: 180px; width: 840px; height: 478px;
    background: var(--card-bg);
    overflow: hidden;
  }
  .card--front { top: 100px; }
  .card--back { top: 620px; }

  .brand {
    position: absolute; left: 0; right: 0;
    display: flex; align-items: center; justify-content: center; gap: 14px;
    color: var(--brand-ink);
  }
  .brand__mark { background: var(--brand-green); flex: none; }
  .card--front .brand { top: 160px; font-size: 34px; }
  .card--front .brand__mark { width: 30px; height: 30px; }
  .card--back .brand { top: 240px; font-size: 60px; }
  .card--back .brand__mark { width: 52px; height: 52px; }

  .contact { position: absolute; left: 0; right: 0; text-align: center; }
  .contact__name { top: 230px; font-size: 30px; letter-spacing: -0.3px; }
  .contact__phone { top: 264px; font-size: 21px; letter-spacing: 0.5px; }
  .contact__web { top: 314px; font-size: 18px; line-height: 21px; letter-spacing: -0.3px; }

  .ground { position: absolute; left: 0; right: 0; bottom: 0; height: 123px; }
  .ground__grass {
    height: 65px;
    background: linear-gradient(to bottom, var(--grass-light), var(--grass-mid) 55%, var(--grass-deep));
  }
  .ground__soil { height: 28px; background: var(--soil); }
  .ground__subsoil { height: 30px; background: var(--subsoil); }
</style>
</head>
<body>
  <section class="card card--front">
    <div class="brand"><span class="brand__mark"></span><span class="brand__name">Meadowline Turf</span></div>
    <p class="contact contact__name">Gareth Pellow</p>
    <p class="contact contact__phone">0478559201</p>
    <p class="contact contact__web">email: meadowlineturf@mailbox-example.com<br>www.meadowlineturf.com.au</p>
    <div class="ground">
      <div class="ground__grass" role="img" aria-label="Strip of green grass dotted with white daisies"></div>
      <div class="ground__soil"></div>
      <div class="ground__subsoil"></div>
    </div>
  </section>

  <section class="card card--back">
    <div class="brand"><span class="brand__mark"></span><span class="brand__name">Meadowline Turf</span></div>
    <div class="ground">
      <div class="ground__grass" role="img" aria-label="Strip of green grass dotted with white daisies"></div>
      <div class="ground__soil"></div>
      <div class="ground__subsoil"></div>
    </div>
  </section>
</body>
</html>
```